Gerald Pinnock - Corporate MC & Entertainer

Design a one page A4 flyer
(See Brief Attached)
I'm after a one Page Flyer
A4 Size - One sided
I want the finished artwork in 2 Forms.
1/ One that I could print out myself in a small run ( I have a Dorvan Tint PrintMaster)
or send out as a PDF
2/ A second version that could be printed commercially , so including bleed crop marks so it can be cut to A4 size
I have attached the copy that should be included. (Agency Sweep 2014 WORDS)
If there was too much text to include , we could drop one of the testimonial quotes
I have attached 3 images that could be included if there is room.
If there were too many images I suggest dropping Image 3 ( with bow tie)
As you can see from the copy (or a visit to my website) there are two main services that I provide
Corporate MC Services and Entertainment Services.
These are however intertwined - My MC work often includes some entertaining effects from my ThoughtCatcher Show. I often get booked to MC a conference and provide a show.
I'm after something that is -
Classy , Sophisticated, Smart, perhaps a bit quirky.
Nothing "Magic" like - eg no Rabbits , Wands, puffs of smoke
I have no corporate colour or logo or branding that should be included
You can see some previous flyers here http://www.proflinkora.com/in/geraldpinnock
I like these, but looking for new ideas
Target Market(s)
Corporate , Conference Organisers, Speaker Bureau owners, Large Association Conference committees
Industry/Entity Type
Entertainment
Colors
Designer to choose colors to be used in the design.

```html
<!DOCTYPE html>
<html lang="en">
<head>
<meta charset="utf-8">
<title>Gerald Pinnock – Corporate MC &amp; Entertainer</title>
<link rel="stylesheet" href="https://fonts.googleapis.com/css2?family=Bebas+Neue&family=Open+Sans:ital,wght@0,400;0,700;1,400&display=swap">
<style>
  :root{
    --green:#8dc63f;
    --blue:#27a9e1;
    --ink:#111111;
    --white:#ffffff;
    --stage:#000000;
    --text:#1a1a1a;
  }
  *{margin:0;padding:0;box-sizing:border-box}
  html,body{width:1200px;height:999px;overflow:hidden;background:var(--stage)}
  .flyer{position:absolute;left:270px;top:34px;width:660px;height:931px;background:var(--white);overflow:hidden}
  .display{font-family:"Bebas Neue",Impact,sans-serif;font-weight:400}
  .masthead{position:absolute;left:0;top:0;width:660px;height:104px;background:var(--green);color:var(--white);
    text-align:center;font-size:88px;line-height:112px;letter-spacing:1px}
  .hero{position:absolute;left:0;top:104px;width:660px;height:362px;
    background:radial-gradient(ellipse at 40% 45%,#3a3a3a 0%,#141414 35%,#050505 70%)}
  .hero-tagline{position:absolute;right:24px;top:30px;text-align:right;color:var(--white);line-height:.95}
  .hero-tagline .l1{font-size:58px;display:block}
  .hero-tagline .l2{font-size:44px;display:block}
  .hero-tagline .l3{font-size:94px;display:block;color:var(--green);line-height:.9}
  .hero-role{position:absolute;left:34px;top:288px;color:var(--white);font-family:"Open Sans",Arial,sans-serif;
    font-weight:700;font-size:21px;line-height:31px}
  .strapline{position:absolute;left:0;top:466px;width:660px;height:44px;background:var(--green);color:var(--white);
    font-family:"Open Sans",Arial,sans-serif;font-weight:700;font-size:28px;line-height:44px;text-align:center;letter-spacing:.3px}
  .body-copy{position:absolute;left:22px;top:521px;width:448px;font-family:"Open Sans",Arial,sans-serif;
    font-size:11.6px;line-height:15.5px;color:var(--text);text-align:justify}
  .body-copy p{margin-bottom:15.5px}
  .testimonials{position:absolute;left:22px;top:722px;width:448px;font-family:"Open Sans",Arial,sans-serif;
    font-size:11.6px;line-height:15.5px;color:var(--text);text-align:justify}
  .testimonials h2{font-family:"Bebas Neue",Impact,sans-serif;font-weight:400;color:var(--blue);font-size:27px;line-height:26px;margin-bottom:4px}
  .testimonials blockquote{font-style:italic}
  .testimonials cite{font-style:normal;display:block;margin-bottom:15px}
  .promo{position:absolute;left:473px;top:512px;width:187px;height:136px;background:var(--blue);color:var(--white);text-align:center}
  .promo .q1{display:block;font-size:24px;line-height:24px;margin-top:9px}
  .promo .q2{display:block;font-size:50px;line-height:50px}
  .promo .cta{display:block;font-family:"Open Sans",Arial,sans-serif;font-weight:700;font-size:13px;line-height:19px}
  .stage-photo{position:absolute;left:473px;top:656px;width:187px;height:210px;
    background:radial-gradient(ellipse at 50% 55%,#1d2a55 0%,#0a0d1c 55%,#02030a 100%)}
  .footer{position:absolute;left:0;top:871px;width:660px;height:60px}
  .footer svg{position:absolute;left:0;top:0}
  .footer .phone{position:absolute;left:24px;top:0;line-height:60px;font-family:"Open Sans",Arial,sans-serif;
    font-weight:700;font-size:35px;color:var(--ink)}
  .footer .web{position:absolute;right:24px;top:0;line-height:60px;font-family:"Open Sans",Arial,sans-serif;
    font-weight:700;font-size:26px;color:var(--ink)}
</style>
</head>
<body>
<main class="flyer">
  <header class="masthead display">GERALD PINNOCK</header>

  <section class="hero" role="img" aria-label="Photo of the presenter in a dark suit smiling and pointing beside a lectern microphone against a starry stage backdrop">
    <h1 class="hero-tagline display">
      <span class="l1">AUSTRALIA'S</span>
      <span class="l2">MAGICIAN OF THE</span>
      <span class="l3">MIND</span>
    </h1>
    <p class="hero-role">Corporate MC<br>&amp;&nbsp; Entertainer</p>
  </section>

  <div class="strapline">SOLVING YOUR CONFERENCE PUZZLES!</div>

  <section class="body-copy">
    <p>In the last two years Gerald has been engaged as the Conference MC for events in Hawaii, New Zealand, Hong Kong &amp; all States of Australia.</p>
    <p>He facilitated 24 Australian Major Project Conferences for ExpoVenture and 16 International CEO Summits for Meridian Summits Group.</p>
    <p>In the Australian Corporate Sector, he managed major events for - OzCover Brokers, Insurbrook, HomeHaven Care, Signal Hire, Parish Care and the Greenleaf Growers Association.</p>
    <p>As an Entertainer he cruised the world on several luxury cruise ships, visiting Japan, Korea, China, Tahiti and New Zealand in his travels.</p>
  </section>

  <section class="testimonials">
    <h2>RECENT TESTIMONIALS</h2>
    <blockquote>"A big thank you for a really good job on Friday night which was carried out with aplomb - well done!"</blockquote>
    <cite>- Greenleaf Growers Association</cite>
    <blockquote>"Huge thanks for your professionalism with the Awards, getting a laugh from everyone and in general creating an atmosphere that was enjoyable and relaxed!"</blockquote>
    <cite>- HomeHaven Care</cite>
  </section>

  <aside class="promo">
    <span class="q1 display">WHAT'S COMING UP IN</span>
    <span class="q2 display">2014?</span>
    <span class="cta">Get involved at<br>www.GeraldPinnock.com</span>
  </aside>

  <div class="stage-photo" role="img" aria-label="Photo of the presenter on stage with arms outstretched in front of a starry backdrop"></div>

  <footer class="footer">
    <svg width="660" height="60" viewBox="0 0 660 60" aria-hidden="true">
      <rect x="0" y="0" width="660" height="60" fill="var(--green)"/>
      <polygon points="0,0 310,0 295,60 0,60" fill="var(--blue)"/>
    </svg>
    <span class="phone">0400 555 218</span>
    <span class="web">www.GeraldPinnock.com</span>
  </footer>
</main>
</body>
</html>
```